DM - management consultant

Business card - contemporary design

Front info
Dorian Maples

(Address not necessary)
PO Box 7386
Belmont, CA 94002

(650) 555-0143
dm@dorianmapl.es

Chirpline: dmq527
Circleboard: /Dorian.Maples
Workgraph: /in/dorianmaples

Back or Front
www.dorianmaples.net
Facilitation & coaching, change management, strategic partnerships, business improvement

Target Market(s)

High tech businesses - mostly startups in Silicon Valley

Industry/Entity Type

Business

Font styles to use
Sans Serif

Colors

Designer to choose colors to be used in the design.

```html
<!DOCTYPE html>
<html lang="en">
<head>
<meta charset="utf-8">
<title>Dorian Maples – Business Card</title>
<link rel="stylesheet" href="https://fonts.googleapis.com/css2?family=Arimo:wght@400;700&display=swap">
<style>
  :root {
    --backdrop: #cfe9f0;
    --card: #000000;
    --ink: #ffffff;
    --art-light: #5a5a5a;
    --art-dark: #1c1c1c;
  }
  * { margin: 0; padding: 0; box-sizing: border-box; }
  html, body { width: 1200px; height: 1200px; overflow: hidden; }
  body {
    background: var(--backdrop);
    font-family: "Arimo", Arial, sans-serif;
    color: var(--ink);
    position: relative;
  }
  .card {
    position: absolute;
    width: 840px;
    height: 480px;
    background: var(--card);
    overflow: hidden;
  }
  .card--front { left: 60px; top: 100px; }
  .card--back { left: 300px; top: 620px; }

  .hand-art {
    position: absolute;
    right: 0;
    top: 0;
    width: 260px;
    height: 190px;
    display: block;
  }
  .name-tag {
    position: absolute;
    left: 300px;
    top: 110px;
    width: 280px;
    height: 110px;
    border: 6px solid var(--ink);
    border-radius: 18px;
    padding: 14px 0 0 16px;
  }
  .name-tag__name {
    font-weight: 700;
    font-size: 36px;
    line-height: 1;
    white-space: nowrap;
  }
  .name-tag__role {
    margin-top: 10px;
    font-weight: 700;
    font-size: 16px;
    white-space: nowrap;
  }

  .services {
    position: absolute;
    left: 200px;
    top: 300px;
    font-size: 22px;
    line-height: 1.4;
    letter-spacing: 0.6px;
  }
  .website {
    position: absolute;
    right: 70px;
    top: 390px;
    font-weight: 700;
    font-size: 22px;
    letter-spacing: 0.5px;
  }

  .direct {
    position: absolute;
    right: 50px;
    top: 320px;
    font-weight: 700;
    font-size: 21px;
    line-height: 1.2;
  }
  .social {
    position: absolute;
    left: 115px;
    bottom: 40px;
    font-weight: 700;
    font-size: 21px;
    line-height: 1.2;
    list-style: none;
  }
</style>
</head>
<body>

  <section class="card card--front" aria-label="Card front">
    <svg class="hand-art" viewBox="0 0 260 190" role="img" aria-label="White line drawing of a hand holding the name tag">
      <defs>
        <linearGradient id="hand-tone-front" x1="0" y1="0" x2="1" y2="1">
          <stop offset="0" stop-color="#5a5a5a"/>
          <stop offset="1" stop-color="#1c1c1c"/>
        </linearGradient>
      </defs>
      <rect width="260" height="190" fill="url(#hand-tone-front)"/>
    </svg>
    <div class="name-tag">
      <div class="name-tag__name">Dorian Maples</div>
      <div class="name-tag__role">management consultant</div>
    </div>
    <p class="services">
      Facilitation &amp; coaching, Change management<br>
      Strategic partnerships, Business improvement
    </p>
    <p class="website">www.dorianmaples.net</p>
  </section>

  <section class="card card--back" aria-label="Card back">
    <svg class="hand-art" viewBox="0 0 260 190" role="img" aria-label="White line drawing of a hand holding the name tag">
      <defs>
        <linearGradient id="hand-tone-back" x1="0" y1="0" x2="1" y2="1">
          <stop offset="0" stop-color="#5a5a5a"/>
          <stop offset="1" stop-color="#1c1c1c"/>
        </linearGradient>
      </defs>
      <rect width="260" height="190" fill="url(#hand-tone-back)"/>
    </svg>
    <div class="name-tag">
      <div class="name-tag__name">Dorian Maples</div>
      <div class="name-tag__role">management consultant</div>
    </div>
    <p class="direct">
      (650) 555-0143<br>
      dm@dorianmapl.es
    </p>
    <ul class="social">
      <li>Chirpline: dmq527</li>
      <li>Circleboard: /Dorian.Maples</li>
      <li>Workgraph: /in/dorianmaples</li>
    </ul>
  </section>

</body>
</html>
```